Dust N Gone! Cleaning needs a flyer!

We have started a cleaning business DUST N GONE! Cleaning, and had a new logo design for it.
We would like a flyer designed to present to businesses that represents our professionalism, quality of service, security and value for money.
We would like a flyer that we can present to both our residential clients and business owners alike.
We will use this flyer for the next 2 years without having to make changes.
I'm happy for the designer to come up with their own wording if necessary.
Updates

Hello everyone!

In addition to the information I have already provided, please see below for more information to be included on the design for our flyer.

Thank you in advance.

Don’t read this unless your current cleaners are AMAZING!

Are you still reading? Now for the good news! Announcing the arrival of the amazing cleaning team of Dust N Gone! Cleaning. They’re the BEST in the Wimmera and we personally guarantee it.

We offer an ultimate service that NO other cleaning company in the Wimmera can offer; high quality cleaning of your home or business, carpet dry cleaning and pest control. All of these services can be completed at a time that is most convenient to you.

From wiping benches to washing windows, from dusting skirting boards to dry cleaning your carpets, from bathrooms to bugs, we really are your ONE stop shop.

Why choose the greatest cleaning company in the Wimmera?

For over 18 years, we have built a reputation on honesty and trust in the residential and commercial services. Our business is to know what people expect when we walk in to your home or business.

With our vast experience and knowledge, we know how to find the best people for the job, how to identify the best products for the clean, we use the newest of technology and equipment and have the best attitudes in town.

Local people, local business that you can rely on because we are also Dust N Gone! Pest Control & Fibrela all rolled in to your ONE stop shop for residential services.

Call us to discuss how we can give you the quality you demand.

Residential Cleaning                                                       Commercial Cleaning                                     

General house cleaning                                                  Business Premises          

Home help                                                                         Vacated properties

Rental vacancies                                                               Schools

Post renovation cleans                                                     Motels/Hotels

 

                                   

Target Market(s)

Business owners, commercial properties, home owners (women aged between 30 - 80y/o)

Industry/Entity Type

Residential

Requirements
Must have
• Incorporate our logo and colours.
Double sided.
Images of interiors of both home & office.
Catch phrase: "You demand quality ..... we guarantee it!"
Address: 22-26 Wattlegum St, Horsham VIC 3400
Phone: 1300 482 316
ABN: 47 308 562 194
We complete the ususal cleaning such as:
General House cleaning
Commercial Cleaning
Rental Properties
Business Premises
Other services we offer is:
Carpet dry cleaning
Upholstery cleaning
Dust N Gone! Mite Chasers pest control
Window cleaning.

```html
<!DOCTYPE html>
<html lang="en">
<head>
<meta charset="utf-8">
<title>Dust N Gone! Cleaning – Flyer</title>
<link rel="stylesheet" href="https://fonts.googleapis.com/css2?family=Open+Sans:wght@600;700&family=Questrial&display=swap">
<style>
  :root{
    --pink:#f01fe6;
    --ink:#2e2e2e;
    --black:#000;
    --white:#fff;
    --head-font:"Questrial", sans-serif;
    --body-font:"Open Sans", sans-serif;
  }
  html,body{margin:0;padding:0;width:1200px;height:1105px;overflow:hidden;background:var(--white);}
  .flyer{position:relative;width:1112px;height:1024px;transform:scale(1.0791);transform-origin:0 0;background:var(--white);overflow:hidden;}
  .backdrop{position:absolute;inset:0;width:1112px;height:1024px;}
  .headline{position:absolute;margin:0;font-family:var(--head-font);font-weight:400;color:var(--pink);white-space:nowrap;line-height:1;}
  .headline--sm{font-size:37.8px;}
  .headline--lg{font-size:51px;}
  .body-line{position:absolute;margin:0;font-family:var(--body-font);font-weight:600;font-size:21.6px;line-height:30px;color:var(--ink);white-space:nowrap;}
  .brand-name{position:absolute;left:14px;margin:0;font-family:var(--body-font);font-weight:700;color:var(--white);white-space:nowrap;line-height:1;}
  .brand-name--main{top:880px;font-size:54px;}
  .brand-name--sub{top:952px;font-size:36px;}
  .tagline{position:absolute;margin:0;font-family:var(--body-font);font-weight:700;font-size:37px;color:var(--white);white-space:nowrap;line-height:1;}
</style>
</head>
<body>
<div class="flyer">
  <svg class="backdrop" viewBox="0 0 1112 1024" aria-hidden="true">
    <path class="swoosh-top" d="M700 0 C 850 45, 1000 78, 1112 72 L1112 0 Z" fill="var(--black)"/>
    <path class="base-band" d="M0 640 C 150 730, 330 860, 560 852 C 790 842, 990 770, 1112 690 L1112 1024 L0 1024 Z" fill="var(--black)"/>
    <path class="divider-curve" d="M578 62 C 538 250, 528 380, 574 480 C 620 580, 602 680, 590 775" fill="none" stroke="var(--pink)" stroke-width="3"/>
    <g class="tagline-frame" stroke="var(--pink)" stroke-width="3" fill="none">
      <path d="M830 882 L570 882 L570 935"/>
      <path d="M650 1003 L1060 1003 L1060 945"/>
    </g>
  </svg>

  <h1 class="headline headline--sm" style="left:20px;top:33px;">Don’t read this unless your</h1>
  <p class="headline headline--sm" style="left:158px;top:78px;">current cleaners are</p>
  <p class="headline headline--lg" style="left:290px;top:128px;">AMAZING!</p>

  <p class="body-line" style="left:35px;top:185px;">Are you still reading? Now for the good news!</p>
  <p class="body-line" style="left:35px;top:215px;">Announcing the arrival of the amazing cleaning</p>
  <p class="body-line" style="left:35px;top:245px;">team of Dust N Gone! Cleaning. They’re the BEST</p>
  <p class="body-line" style="left:35px;top:275px;">in the Wimmera and we personally guarantee it.</p>

  <p class="body-line" style="left:35px;top:335px;">We offer an ultimate service that NO other</p>
  <p class="body-line" style="left:35px;top:365px;">cleaning company in the Wimmera can offer,</p>
  <p class="body-line" style="left:35px;top:395px;">high quality cleaning of your home or business,</p>
  <p class="body-line" style="left:35px;top:425px;">carpet dry cleaning and pest control. All of these</p>
  <p class="body-line" style="left:35px;top:455px;">services can be completed at a time that is most</p>
  <p class="body-line" style="left:35px;top:485px;">convenient to you.</p>

  <p class="body-line" style="left:35px;top:545px;">From wiping benches to washing windows, from</p>
  <p class="body-line" style="left:35px;top:575px;">dusting skirting boards to dry cleaning your carpets,</p>
  <p class="body-line" style="left:35px;top:605px;">from bathrooms to bugs, we really are your ONE</p>
  <p class="body-line" style="left:35px;top:635px;">stop shop.</p>

  <p class="body-line" style="left:575px;top:137px;">For over 18 years, we have built a reputation</p>
  <p class="body-line" style="left:575px;top:167px;">on honesty and trust in the residential and</p>
  <p class="body-line" style="left:575px;top:197px;">services. Our business is to know what people</p>
  <p class="body-line" style="left:575px;top:227px;">expect when we walk to your home or business.</p>

  <p class="body-line" style="left:580px;top:287px;">With our vast experience and knowledge, we</p>
  <p class="body-line" style="left:592px;top:317px;">know how to find the best people for the</p>
  <p class="body-line" style="left:604px;top:347px;">job, how to identify the best products for</p>
  <p class="body-line" style="left:620px;top:377px;">clean, we use the newest of technology</p>
  <p class="body-line" style="left:637px;top:407px;">and equipment and have the best</p>
  <p class="body-line" style="left:643px;top:437px;">attitudes in town.</p>

  <p class="body-line" style="left:643px;top:497px;">Local people, local business that you can</p>
  <p class="body-line" style="left:650px;top:527px;">rely on because we are also Dust N Gone!</p>
  <p class="body-line" style="left:656px;top:557px;">Pest Control &amp; Fibrela all rolled in to</p>
  <p class="body-line" style="left:654px;top:587px;">your ONE stop shop for residential services.</p>

  <h2 class="headline headline--sm" style="right:7px;top:640px;">Why choose the greatest</h2>
  <p class="headline headline--sm" style="left:670px;top:685px;">cleaning company in</p>
  <p class="headline headline--lg" style="left:650px;top:733px;">Wimmera?</p>

  <p class="brand-name brand-name--main">DUST N GONE!</p>
  <p class="brand-name brand-name--sub">Cleaning</p>

  <p class="tagline" style="left:587px;top:893px;">You demand Quality...</p>
  <p class="tagline" style="right:64px;top:952px;">We guarantee it!</p>
</div>
</body>
</html>
```